Blow Dry Bar Business Cards

These cards must be eye catching and modern.
You must be willing to work fast and make changes.

Winner will be offered other projects

Files 1 THIS IS THE STYLE CARDS I AM INTRESTED IN!!!
Please be creative, I am paying for my own eye catching design. I need files to be prisma press ready.

COLORS THAT ARE PAINTED INSIDE MY SHOP:
- - - http://www.brenwickcoatings.example/en/explore-colors/painter/color-selector.html?colors=4007-3C

- - - http://www.tarnellhues.example/color/paint-colors/quiet-harbor-d58-2

I want the business cards sleek and modern if you use the logo please correct imperfections. I added the part that says Blow Dry Bar (see website).
Do not be afraid to separate the blow dryer from the name to make the cards look like the file with the pink elephant.

SHOULD INCLUDE
*Blow Dryer (we are a blow dry bar not a salon we do not cut or color so do not include sheers of any kind)
*BUSINESS NAME: Simply Silken Waves - Blow Dry Bar (PLEASE SEE MY WEBSITE)
* Website: SIMPLYSILKENWAVES.EXAMPLE
*Phone number (555) 014-2763
Updates

Prisma press said it can be submitted in JPG

http://www.tarnellhues.example/color/paint-colors/quiet-harbor-d58-2 http://www.brenwickcoatings.example/en/explore-colors/painter/color-selector.html?colors=4007-3C ^^^^ These links will take you to the color paint that is painted inside my shop.

Target Market(s)

AGES 18 - 55 WOMEN
HIGH END MARKET

Industry/Entity Type

Salon

Requirements
Must have
• SEE COLOR EXAMPLE FILE
BLOW DRYER
UNIQUE
I LIKE THE CARD WITH THE PINK ELEPHANT THE BEST
Nice to have
• BE AS CREATIVE AND MODERN AS POSSIBLE DO NOT COPY ANY OF THE CARDS BELOW.
Should not have
• SCISSORS
PINK

```html
<!DOCTYPE html>
<html lang="en">
<head>
<meta charset="utf-8">
<title>Silken Waves – Business Cards</title>
<link rel="stylesheet" href="https://fonts.googleapis.com/css2?family=Cinzel:wght@400;600&family=Libre+Baskerville&display=swap">
<style>
  :root{
    --backdrop:#ebe6e0;
    --maroon:#561312;
    --bronze:#a5703f;
    --tan:#c99a68;
    --gold:#d7a648;
    --gold-light:#f1d79a;
    --yellow:#f3d400;
    --paper:#ffffff;
    --ink:#2a2321;
  }
  *{margin:0;padding:0;box-sizing:border-box}
  html,body{width:1200px;height:848px;overflow:hidden;background:var(--backdrop)}
  .canvas{position:relative;width:1200px;height:848px}
  .card{
    position:absolute;width:540px;height:309px;top:270px;
    border-radius:18px;overflow:hidden;background:var(--paper);
    box-shadow:0 10px 26px rgba(60,35,20,.28);
  }
  .card--front{left:40px}
  .card--back{left:620px}
  .card__art{position:absolute;inset:0;width:100%;height:100%}
  .contact{
    position:absolute;left:34px;top:30px;list-style:none;
    font-family:"Cinzel",serif;color:var(--yellow);font-size:15.5px;letter-spacing:.4px;line-height:24px;
  }
  .contact li{display:flex;align-items:flex-start;gap:10px}
  .contact svg{width:15px;height:15px;margin-top:4px;flex:none;fill:var(--yellow)}
  .contact .indent{padding-left:25px}
  .brand{
    position:absolute;font-family:"Cinzel",serif;font-weight:600;color:var(--yellow);
    white-space:nowrap;display:flex;align-items:center;gap:10px;line-height:1;
  }
  .card--front .brand{right:28px;bottom:24px;font-size:30px}
  .card--back .brand{left:24px;top:138px;font-size:27px}
  .brand__dot{width:11px;height:11px;border-radius:50%;background:var(--yellow)}
  .offers{
    position:absolute;right:18px;top:40px;width:212px;text-align:right;
    font-family:"Libre Baskerville",serif;font-size:8px;line-height:13px;color:var(--ink);text-transform:uppercase;
  }
  .offers p + p{margin-top:1px}
</style>
</head>
<body>
<main class="canvas">

  <section class="card card--front" aria-label="Business card front">
    <svg class="card__art" viewBox="0 0 540 309" preserveAspectRatio="none" aria-hidden="true">
      <defs>
        <radialGradient id="frontFill" cx="0.85" cy="0" r="1.05">
          <stop offset="0" stop-color="#d7ad80"/>
          <stop offset="0.45" stop-color="#a5703f"/>
          <stop offset="1" stop-color="#561312"/>
        </radialGradient>
      </defs>
      <path d="M0,0 H540 V40 C480,34 440,70 395,135 C350,200 300,222 235,218 C160,214 90,168 0,158 Z" fill="url(#frontFill)"/>
      <path d="M0,164 C90,176 160,222 235,226 C300,230 352,204 398,140 C440,80 480,44 540,48" fill="none" stroke="#561312" stroke-width="7"/>
      <path d="M0,170 C90,184 162,232 236,236 C304,240 358,212 404,146 C446,86 484,54 540,58" fill="none" stroke="#d7a648" stroke-width="2.5"/>
      <path d="M0,160 C90,172 160,218 235,222 C300,226 350,200 396,137" fill="none" stroke="#f1d79a" stroke-width="1.2"/>
    </svg>
    <ul class="contact">
      <li><svg viewBox="0 0 24 24"><path d="M6.6 10.8a15 15 0 0 0 6.6 6.6l2.2-2.2a1 1 0 0 1 1-.25 11.4 11.4 0 0 0 3.6.57 1 1 0 0 1 1 1V20a1 1 0 0 1-1 1A17 17 0 0 1 3 4a1 1 0 0 1 1-1h3.5a1 1 0 0 1 1 1c0 1.25.2 2.45.57 3.57a1 1 0 0 1-.25 1z"/></svg>(555) 014-2763</li>
      <li><svg viewBox="0 0 24 24"><path d="M12 2a10 10 0 1 0 0 20 10 10 0 0 0 0-20zm6.9 6h-3a15.6 15.6 0 0 0-1.4-3.6A8 8 0 0 1 18.9 8zM12 4c.8 1.2 1.5 2.5 1.9 4h-3.8c.4-1.5 1.1-2.8 1.9-4zM4.3 14a8 8 0 0 1 0-4h3.4a16 16 0 0 0 0 4zm.8 2h3a15.6 15.6 0 0 0 1.4 3.6A8 8 0 0 1 5.1 16zm3-8h-3a8 8 0 0 1 4.4-3.6A15.6 15.6 0 0 0 8.1 8zM12 20c-.8-1.2-1.5-2.5-1.9-4h3.8c-.4 1.5-1.1 2.800-1.9 4zm2.3-6H9.7a14.7 14.7 0 0 1 0-4h4.6a14.7 14.7 0 0 1 0 4zm.3 5.6a15.6 15.6 0 0 0 1.4-3.6h3a8 8 0 0 1-4.4 3.6zM16.3 14a16 16 0 0 0 0-4h3.4a8 8 0 0 1 0 4z"/></svg>www.simplysilkenwaves.example</li>
      <li><svg viewBox="0 0 24 24"><path d="M2 5h20v14H2zm2 2v.5l8 5 8-5V7zm0 2.8V17h16V9.8l-8 5z"/></svg>info@simplysilkenwaves.example</li>
      <li><svg viewBox="0 0 24 24"><path d="M12 2a7 7 0 0 0-7 7c0 5.2 7 13 7 13s7-7.8 7-13a7 7 0 0 0-7-7zm0 9.5A2.5 2.5 0 1 1 12 6.5a2.5 2.5 0 0 1 0 5z"/></svg>88 Marlow Bend Drive Suite</li>
      <li class="indent">11 Cedar Hollow, Texas 70123</li>
    </ul>
    <div class="brand"><span class="brand__dot"></span>Silken Waves</div>
  </section>

  <section class="card card--back" aria-label="Business card back">
    <svg class="card__art" viewBox="0 0 540 309" preserveAspectRatio="none" aria-hidden="true">
      <defs>
        <radialGradient id="backFill" cx="0.6" cy="0" r="1.05">
          <stop offset="0" stop-color="#d7ad80"/>
          <stop offset="0.45" stop-color="#a5703f"/>
          <stop offset="1" stop-color="#561312"/>
        </radialGradient>
      </defs>
      <path d="M0,0 H360 C320,10 300,70 280,140 C258,210 220,245 140,252 C90,256 40,259 0,264 Z" fill="url(#backFill)"/>
      <path d="M366,0 C327,14 307,74 287,144 C265,216 225,252 142,259 C90,263 40,266 0,271" fill="none" stroke="#561312" stroke-width="7"/>
      <path d="M376,0 C337,18 317,78 297,148 C275,224 231,262 144,269 C90,273 40,276 0,281" fill="none" stroke="#d7a648" stroke-width="2.5"/>
      <path d="M357,0 C317,10 297,70 277,138" fill="none" stroke="#f1d79a" stroke-width="1.2"/>
    </svg>
    <div class="brand"><span class="brand__dot"></span>Silken Waves</div>
    <div class="offers">
      <p>Monday Madness</p>
      <p>10% off all products purchased in store</p>
      <p>Thrifty Tuesday</p>
      <p>$5.00 off your blow out service when you add any one upper</p>
      <p>Winedown Wednesday</p>
      <p>Bring a friend, 2 blow outs for $60.00+tax</p>
    </div>
  </section>

</main>
</body>
</html>
```